Xtreme Web Design

We require a web designer to create a new website design template for our business. A mixture of stock images, our images and graphic will be used. We would like a 'home' page that will stand out and a common base page design for all other pages in our site. We need to keep our current logo and will be looking for designs that stand out and relate directly to our industry (xtreme fast indoor go kart racing). We have also attached our current font that is used in our brochures and may or may not be used in your design.
We are currently opening another new facility and will be able to provide a lot of good quality racing, facility related and go kart images soon, but until then please obtain general images or images from our current site (www.brimblefrost.com.au) as required.
The design we need to be unique and sharp with options/ideas of various jquery plugins that we will utilize.
Project Deadline Extended
Reason: Being close to the busy xmas period, we have not been able to give fair feedback to some designs and would like to extend the deadline to allow for this. I thank you for your understanding.

```html
<!DOCTYPE html>
<html lang="en">
<head>
<meta charset="utf-8">
<title>Brimblefrost – Special Offers</title>
<link rel="stylesheet" href="https://fonts.googleapis.com/css2?family=Arimo:wght@400;700&family=Exo+2:ital,wght@0,300;1,400&family=Rubik+Dirt&display=swap">
<style>
:root{
  --page:#f3f3f3;
  --panel:#fafafa;
  --stripe:#00aeef;
  --navy:#13168a;
  --navy-dark:#0c0f6b;
  --cyan:#1eaee8;
  --text:#2a2a2a;
  --bar-top:#5a5a55;
  --bar-bottom:#2b2b29;
  --menu:#1f1f1f;
  --menu-active:#0795cf;
  --footer-top:#2e2e2e;
  --footer-bottom:#171717;
  --muted:#8c8c8c;
  --rule:#dcdcdc;
}
*{margin:0;padding:0;box-sizing:border-box}
html,body{width:1200px;height:808px;overflow:hidden;background:var(--page)}
body{position:relative;font-family:"Arimo",Arial,sans-serif;color:var(--text)}
.backdrop{position:absolute;left:0;top:0}
.abs{position:absolute}

/* header bar */
.top-bar{left:411px;top:0;width:695px;height:48px;background:linear-gradient(var(--bar-top),var(--bar-bottom));clip-path:polygon(14px 0,100% 0,100% 100%,0 100%)}
.follow{left:474px;top:12px;font-family:"Exo 2",sans-serif;font-weight:300;font-size:20px;color:#fff}
.social-square{top:11px;width:26px;height:26px;border-radius:3px}
.social-square.one{left:571px;background:#5cc8ef}
.social-square.two{left:611px;background:#3b5a9a}
.top-phone{left:875px;top:13px;font-family:"Exo 2",sans-serif;font-weight:300;font-size:19px;color:#fff}
.top-phone-icon{left:1046px;top:11px}

/* brand */
.brand{left:70px;top:50px;display:flex;align-items:center;gap:8px;font-family:"Arimo",sans-serif;font-weight:700;font-size:25px;color:var(--navy);letter-spacing:1px}
.brand .dot{width:14px;height:14px;border-radius:50%;background:var(--navy)}
.brand-sub{left:70px;top:82px;font-weight:700;font-size:10px;letter-spacing:1.6px;color:var(--navy)}

/* navigation */
.nav-item{left:70px;height:42px;background:linear-gradient(var(--navy),var(--navy-dark));font-family:"Rubik Dirt",sans-serif;font-size:22px;color:#fff;display:flex;align-items:center;padding-left:34px;letter-spacing:1px}
.nav-item::before{content:"";position:absolute;left:14px;top:17px;border-left:7px solid #fff;border-top:4px solid transparent;border-bottom:4px solid transparent}
.dropdown{left:164px;top:326px;width:141px;height:147px;background:var(--menu);opacity:.95;padding-top:11px}
.dropdown a{display:block;height:26px;line-height:26px;padding-left:12px;font-size:12.5px;color:#fff;text-decoration:none}
.dropdown a.active{background:var(--menu-active)}

/* content */
.content{left:403px;top:76px;width:450px}
.page-title{font-family:"Rubik Dirt",sans-serif;font-weight:400;font-size:29px;color:var(--navy);margin-bottom:4px;margin-left:3px}
.offer-title{font-family:"Exo 2",sans-serif;font-style:italic;font-weight:400;font-size:19px;color:var(--cyan);letter-spacing:.6px;margin:0 0 6px 3px}
.conditions{font-weight:700;font-size:13.5px;margin:0 0 2px 3px}
.offer p{font-size:14px;line-height:21px;margin-bottom:8px}
.offer ul{list-style:none;margin-bottom:22px}
.offer li{position:relative;font-size:14px;line-height:26px;padding-left:17px}
.offer li::before{content:"";position:absolute;left:6px;top:11px;width:4px;height:4px;border-radius:50%;background:#666}
.divider{left:863px;top:79px;width:1px;height:594px;background:var(--rule)}
.gallery-photo{left:891px;width:198px;height:130px}

/* footer */
.footer{left:0;top:714px;width:1200px;height:94px;background:linear-gradient(var(--footer-top),var(--footer-bottom))}
.footer-brand{left:68px;top:733px;display:flex;align-items:center;gap:8px;font-weight:700;font-size:25px;color:#9a9a9a;letter-spacing:1px}
.footer-brand .dot{width:14px;height:14px;border-radius:50%;background:#9a9a9a}
.footer-brand-sub{left:68px;top:766px;font-weight:700;font-size:10px;letter-spacing:1.6px;color:#9a9a9a}
.talk{left:366px;top:731px;font-family:"Exo 2",sans-serif;font-weight:300;font-size:18px;color:var(--muted)}
.talk-icon{left:455px;top:729px}
.footer-phone{left:481px;top:720px;font-family:"Exo 2",sans-serif;font-weight:300;font-size:38px;color:var(--muted);letter-spacing:-1px}
.footer-rule{left:366px;top:772px;width:452px;border-top:1px dotted #555}
.legal{left:366px;top:783px;font-size:11px;color:#777;word-spacing:1px}
.legal .mark{color:#aaa;font-size:12px;margin:0 6px}
.social-circle{top:731px;width:30px;height:30px;border-radius:50%;background:#7d7d7d}
</style>
</head>
<body>

<svg class="backdrop" width="1200" height="714" aria-hidden="true">
  <rect x="342" y="0" width="858" height="714" fill="#ffffff"/>
  <rect x="400" y="48" width="706" height="666" fill="var(--panel)"/>
  <polygon points="342,0 426,0 194,714 109,714" fill="var(--stripe)"/>
</svg>

<div class="abs top-bar"></div>
<div class="abs follow">Follow Us</div>
<div class="abs social-square one"></div>
<div class="abs social-square two"></div>
<div class="abs top-phone">+1 1800 555 0142</div>
<svg class="abs top-phone-icon" width="28" height="26" viewBox="0 0 28 26" aria-hidden="true">
  <path d="M6 4c-3 2-3 6 0 11s8 8 11 7l2-3-4-3-2 2c-2-1-4-3-5-5l2-2-3-4z" fill="#d8d8d8"/>
  <path d="M16 6a6 6 0 0 1 6 6M16 2a10 10 0 0 1 10 10" stroke="#d8d8d8" stroke-width="2" fill="none"/>
</svg>

<div class="abs brand">BRIMBLEFROST<span class="dot"></span></div>
<div class="abs brand-sub">INDOOR KART RACING</div>

<nav>
  <div class="abs nav-item" style="top:174px;width:247px;clip-path:polygon(0 0,100% 0,93% 100%,0 100%)">Pricing</div>
  <div class="abs nav-item" style="top:232px;width:227px;clip-path:polygon(0 0,100% 0,93% 100%,0 100%)">Specials</div>
  <div class="abs nav-item" style="top:286px;width:208px;clip-path:polygon(0 0,100% 0,93% 100%,0 100%)">Group Events</div>
  <div class="abs nav-item" style="top:344px;width:188px;clip-path:polygon(0 0,100% 0,93% 100%,0 100%)">Locations</div>
  <div class="abs nav-item" style="top:402px;width:170px;clip-path:polygon(0 0,100% 0,93% 100%,0 100%)">About Us</div>
  <div class="abs dropdown">
    <a href="#">Birthday Parties</a>
    <a href="#" class="active">Bachelor Parties</a>
    <a href="#">Work Social Events</a>
    <a href="#">Corporate Functions</a>
    <a href="#">Local Sporting Clubs</a>
  </div>
</nav>

<main class="abs content">
  <h1 class="page-title">Special Offers</h1>
  <section class="offer">
    <h2 class="offer-title">$5 off Weekday Grid Prix</h2>
    <h3 class="conditions">Conditions:</h3>
    <ul>
      <li>Must mention offer when booking</li>
      <li>Not available weekends or public holidays</li>
      <li>Min 6 drivers must race</li>
      <li>$10 deposit required for each driver when making booking</li>
      <li>Not valid through Dec/Jan</li>
    </ul>
  </section>
  <section class="offer">
    <h2 class="offer-title">Free Function Room</h2>
    <p>Book a weekday Grand Prix and receive free access to the function room overlooking the track.</p>
    <h3 class="conditions">Conditions:</h3>
    <ul>
      <li>Must mention offer when booking</li>
      <li>Not available weekends or public holidays</li>
      <li>Min 12 drivers must race</li>
      <li>$10 deposit required for each driver when making booking</li>
      <li>No BYO food allowed in function room</li>
      <li>Not valid through Dec/Jan</li>
    </ul>
  </section>
</main>

<div class="abs divider"></div>
<div class="abs gallery-photo" style="top:79px;background:linear-gradient(135deg,#d9d9d9,#6b6f78 60%,#9a2a30)" role="img" aria-label="Function room interior with tables and red lounge"></div>
<div class="abs gallery-photo" style="top:229px;background:linear-gradient(#d8dde0,#8b7f76 55%,#4d4a52)" role="img" aria-label="Birthday group posing in the venue lounge"></div>
<div class="abs gallery-photo" style="top:380px;background:linear-gradient(#e4e6e8,#8d9094 55%,#3f4650)" role="img" aria-label="Group of drivers posing after a race"></div>
<div class="abs gallery-photo" style="top:530px;background:linear-gradient(#3e8fd6,#7aa2b8 45%,#5b7a3a 75%,#d7c43a)" role="img" aria-label="Venue building exterior with hedges and blue sky"></div>

<footer>
  <div class="abs footer"></div>
  <div class="abs footer-brand">BRIMBLEFROST<span class="dot"></span></div>
  <div class="abs footer-brand-sub">INDOOR KART RACING</div>
  <div class="abs talk">Talk to us!</div>
  <svg class="abs talk-icon" width="16" height="30" viewBox="0 0 16 30" aria-hidden="true">
    <path d="M8 2h5v8H9c-1 3-1 7 0 10h4v8H8C3 24 3 6 8 2z" fill="var(--muted)"/>
  </svg>
  <div class="abs footer-phone">800 555 019</div>
  <div class="abs footer-rule"></div>
  <div class="abs legal">©2013 <span class="mark">BRIMBLEFROST</span> All rights reserved. &nbsp;Privacy Policy &nbsp;| &nbsp;Terms &amp; Conditions</div>
  <div class="abs social-circle" style="left:940px"></div>
  <div class="abs social-circle" style="left:974px"></div>
  <div class="abs social-circle" style="left:1008px"></div>
  <div class="abs social-circle" style="left:1042px"></div>
  <div class="abs social-circle" style="left:1076px"></div>
</footer>

</body>
</html>
```